If everything digital fails, here's what to do

Hi, I would like a poster / infographic of a list of practical actions people could take in case the internet stops working. I've put together a list of 8 areas, with the situation for each, and the mitigation actions folks can take - I need it presented in a clear and aesthetically pleasing way. I will send you the file with the full text so you can include it all

General population, but likely people who are safety conscious and want to protect themselves and learn more about what to do to be tech literate and prepared

Tech / Cyber / Public safety / Civic tech

Sans Serif

• It's a lot of text, so I think the important thing is to have it all in one poster, or in a series of similar pages
• I would like it to be a bit brooding, but also elicit competence and that some experts have thought about this and it will all be okay
• I don't want it to look cartoonish, or cheap - less is more is sort of what I'm looking for

```html
<!DOCTYPE html>
<html lang="en">
<head>
<meta charset="utf-8">
<title>If Everything Digital Fails – Here's What To Do</title>
<link href="https://fonts.googleapis.com/css2?family=Bebas+Neue&family=Poppins:ital,wght@0,400;1,400&display=swap" rel="stylesheet">
<style>
  :root{
    --bg-top:#2e1f5e;
    --bg-mid:#1f2260;
    --bg-bottom:#121a3c;
    --panel:#ffffff;
    --navy:#0e1c5e;
    --ink:#ffffff;
    --accent:#35c2f6;
    --ring-bright:#3dcaff;
    --ring-deep:#1b4fb0;
  }
  *{box-sizing:border-box;margin:0;padding:0}
  html,body{width:1200px;height:900px;overflow:hidden}
  body{
    position:relative;
    background:linear-gradient(135deg,var(--bg-top) 0%,var(--bg-mid) 45%,var(--bg-bottom) 100%);
    font-family:"Poppins",sans-serif;
    color:var(--ink);
    font-size:12.3px;
    line-height:14.2px;
    letter-spacing:-0.35px;
  }
  .header{
    position:absolute;
    background:var(--panel);
    color:var(--navy);
    height:61px;
    clip-path:polygon(0 0,calc(100% - 14px) 0,100% 14px,100% 100%,14px 100%,0 calc(100% - 14px));
    display:flex;
    align-items:center;
  }
  .header-icon{width:40px;height:40px;margin:0 8px 0 9px;flex:none}
  .header-icon svg{width:40px;height:40px;stroke:var(--navy);fill:none;stroke-width:1.6;stroke-linecap:round;stroke-linejoin:round}
  .header-text{flex:1;min-width:0}
  .header-title{font-family:"Bebas Neue",sans-serif;font-size:27px;line-height:23px;letter-spacing:0.2px;display:block}
  .header-sub{font-size:15.2px;line-height:14px;letter-spacing:-0.3px;display:block}
  .nowrap{white-space:nowrap}
  .block{position:absolute}
  .refresh{color:var(--accent);font-style:italic;display:block}
  .steps{list-style:none;counter-reset:step}
  .steps li{position:relative;padding-left:13px;margin-bottom:3px;counter-increment:step}
  .steps li::before{content:counter(step) ".";position:absolute;left:0}
  .gap-s{margin-top:4px}

  .col1{left:31px;width:372px}
  .col2{left:479px;width:312px}
  .col3{left:810px;width:372px}
  .head1{left:31px;width:428px}
  .head2{left:479px;width:313px}
  .head3{left:810px;width:359px}

  .hero-ring{
    position:absolute;left:404px;top:254px;width:370px;height:370px;border-radius:50%;
    background:radial-gradient(circle,
      rgba(12,24,70,0.95) 0%,
      rgba(14,30,86,0.95) 50%,
      var(--ring-deep) 54%,
      var(--ring-bright) 57%,
      #1f76d8 60%,
      rgba(30,80,170,0.55) 66%,
      rgba(40,90,190,0.25) 72%,
      rgba(30,60,140,0) 78%);
  }
  .hero{position:absolute;left:439px;top:378px;width:300px;text-align:center;font-family:"Bebas Neue",sans-serif;letter-spacing:0.2px}
  .hero-title{font-size:40px;line-height:32px;font-weight:400}
  .hero-sub{font-size:24px;line-height:24px;margin-top:9px}
  .hero-rule{width:36px;height:2px;background:var(--ink);margin:9px auto 9px}
  .hero-date{font-size:17px;line-height:18px}
</style>
</head>
<body>

<!-- Communications -->
<header class="header head1" style="top:21px">
  <span class="header-icon"><svg viewBox="0 0 40 40"><rect x="11" y="5" width="24" height="17" rx="2"/><path d="M15 10h16M15 14h16M15 18h10"/><rect x="4" y="17" width="20" height="14" rx="2"/><path d="M8 21h12M8 25h9M8 31l-2 5 6-5"/></svg></span>
  <span class="header-text"><span class="header-title">Communications</span><span class="header-sub">Cell phones / land-line phone services<br>have stopped working</span></span>
</header>
<div class="block col1" style="top:92px">
  <ol class="steps">
    <li>Buy a two-way hand-held walkie talkie and share the other with close friends.<span class="refresh">Refresh when? Check to ensure your walkie talkie has working batteries every 12 months (and that you know / remember how the walkie talkie itself works)</span></li>
    <li>Share a ‘third space’ safe spot with close contacts in town where you know you could meet in emergency situations if your home was not safe to remain in. Do the same with neighbours and folks who live in your neighbourhood - have a central gathering spot in your hood that you share with others so you can have a convening spot close by.<span class="refresh">Refresh when? Have a quick reminder conversation about this with your close contacts every 12 months to ensure everyone knows that’s the plan</span></li>
    <li>Have a printed list of your close contacts’ home addresses handy, if you don’t know how to get to their places by heart.<span class="refresh">Refresh when? Print a new such document every 12 months to ensure it stays up to date</span></li>
    <li>Have a list of close contacts that might still have a<br>working landline (ie. rotary, not voip-based),<br>or who have a satellite phone<span class="refresh">Refresh when? Remind yourself of this list and refresh it every 12 months or so</span></li>
    <li>Make a list of the people in your life that you care about that may also be affected, and make sure you include individuals in your community that may be vulnerable in such a disruption<br>(they may be older, may live alone, might need access to supply of medication).<span class="refresh">Refresh when? Remind yourself of this list and refresh it every 12 months or so</span></li>
  </ol>
</div>

<!-- Banking: cash -->
<header class="header head1" style="top:564px">
  <span class="header-icon"><svg viewBox="0 0 40 40"><path d="M5 13 20 5l15 8z"/><path d="M6 13h28M8 16v14M13 16v14M18 16v14M22 16v14M27 16v14M32 16v14M5 31h30M4 35h32"/></svg></span>
  <span class="header-text"><span class="header-title">Banking</span><span class="header-sub">Debit and credit cards have stopped<br>working (in stores; ATMs)</span></span>
</header>
<div class="block col1" style="top:632px">
  <p>Have $500 in cash available in $20 bills.</p>
  <span class="refresh">Refresh when? N/A once done</span>
</div>

<!-- Banking: records -->
<header class="header head1" style="top:673px">
  <span class="header-icon"><svg viewBox="0 0 40 40"><rect x="10" y="6" width="26" height="17" rx="2"/><path d="M10 11h26M24 15h8M24 19h8"/><circle cx="10" cy="24" r="4"/><path d="M3 35c0-5 3-7 7-7s7 2 7 7"/><path d="M31 14v10M33 16h-3a1.5 1.5 0 0 0 0 3h2a1.5 1.5 0 0 1 0 3h-3"/></svg></span>
  <span class="header-text"><span class="header-title">Banking</span><span class="header-sub">Debit and credit cards have stopped working; your bank can’t access its own information (online)</span></span>
</header>
<div class="block col1" style="top:740px;width:370px">
  <p>Print paper records of your banking statements that prove what you have in your bank accounts and store it in a safe place in your living space. Ensure it has dates showing and full amounts, as well as your identifiers (name and account numbers) as well as the institution itself (printed screenshots should work fine if your money is in a few accounts requiring many statements). Note the same goes for your liabilities (i.e. be able to prove how much you had left on your mortgage or other bigger loans, if you have such debt).</p>
  <span class="refresh gap-s">Refresh when? Update this document every 6-12 months</span>
</div>

<!-- Transportation -->
<header class="header head2" style="top:21px">
  <span class="header-icon"><svg viewBox="0 0 40 40"><path d="M4 14l10-9 3 1-5 6 5 1 3-2 1 1-3 4-5 1-9-3z"/><circle cx="31" cy="10" r="6"/><path d="M31 6v8M33 8h-3a1 1 0 0 0 0 2h2a1 1 0 0 1 0 2h-3"/><rect x="14" y="24" width="14" height="10"/><path d="M14 27h-6l-3 4v3h9"/><circle cx="9" cy="35" r="2"/><circle cx="24" cy="35" r="2"/></svg></span>
  <span class="header-text"><span class="header-title">Transportation</span><span class="header-sub nowrap">Gas stations have stopped working</span></span>
</header>
<div class="block col2" style="top:92px">
  <p>(If you own a car) Have a standard 40L gas canister filled with gas and available close by in case needed.</p>
  <span class="refresh gap-s">Refresh when? Use up the gas within 4 months or so, and refill the canister then (i.e. 3 times a year) so that it remains usable</span>
  <p style="margin-top:21px">Safety note: (If relevant) ensure the can is not in a place where kids can get to it, since it’s not safe for kids to be around gas</p>
</div>

<!-- Centre title -->
<div class="hero-ring" role="img" aria-label="Glowing blue concentric rings surrounding the poster title"></div>
<div class="hero">
  <h1 class="hero-title">If everything<br>digital fails</h1>
  <p class="hero-sub">Here’s what to do - a list</p>
  <div class="hero-rule"></div>
  <p class="hero-date">(Last updated: April 2023)</p>
</div>

<!-- Password manager -->
<header class="header head2" style="top:675px">
  <span class="header-icon"><svg viewBox="0 0 40 40"><rect x="6" y="4" width="18" height="32" rx="2"/><path d="M10 10h4v4h-4zM10 17h4v4h-4zM10 24h4v4h-4zM13 32h4"/><rect x="21" y="13" width="12" height="12" rx="1"/><path d="M24 10v3M30 10v3M24 25v3M30 25v3M33 16h3M33 22h3"/></svg></span>
  <span class="header-text"><span class="header-title">Information Management</span><span class="header-sub">Password manager services<br>(cloud) have stopped working</span></span>
</header>
<div class="block col2" style="top:746px">
  <p>Preamble: Many individuals don’t remember their passwords anymore, having password managers generate complicated strings of characters as their passwords for their many digital accounts in their lives. Print a full list of your accounts and their passwords and keep that document safely in your living space.</p>
  <span class="refresh gap-s">Refresh when? Print a new such document every 6 months to ensure the list remains up to date</span>
</div>

<!-- Cloud storage 1 -->
<header class="header head3" style="top:21px">
  <span class="header-icon"><svg viewBox="0 0 40 40"><rect x="9" y="4" width="20" height="27" rx="1"/><rect x="6" y="8" width="20" height="28" rx="1"/><path d="M10 14h12M10 18h12M10 22h12M10 26h8"/><circle cx="33" cy="18" r="3"/><path d="M33 12v2M33 22v2M28 18h-1M39 18h-1"/></svg></span>
  <span class="header-text"><span class="header-title">Information Management</span><span class="header-sub">Cloud storage services have stopped<br>working</span></span>
</header>
<div class="block col3" style="top:92px">
  <p>Do a backup of the important documents that are stored only in your cloud storage (e.g. that important email in your Inkpost; that tax document only issued digitally, etc.)</p>
  <span class="refresh gap-s">Refresh when? Do a backup and update every 6 months</span>
  <p style="margin-top:16px">Note: Since this is a time-consuming exercise but not necessarily the same exercise as #7 below, you could alternate the months when you do one versus the other. For example, you could do this with annual equinoxes: March 21 and Sept 21 (pro tip: star email messages that are important as they arrive, so that you know what needs to be backed up every six months; that way, you don’t have to go searching through your whole inbox)</p>
</div>

<!-- Cloud storage 2 -->
<header class="header head3" style="top:304px">
  <span class="header-icon"><svg viewBox="0 0 40 40"><circle cx="11" cy="11" r="6"/><path d="M9 9a2 2 0 1 1 2 3v1M11 15v0"/><rect x="12" y="14" width="24" height="22" rx="1"/><path d="M20 20h12M20 24h12M20 28h8M16 32l3-3 2 2 3-3"/></svg></span>
  <span class="header-text"><span class="header-title">Information Management</span><span class="header-sub">Cloud storage services have stopped<br>working</span></span>
</header>
<div class="block col3" style="top:374px;font-size:12.1px;line-height:14px">
  <ol class="steps">
    <li>Save all important digital materials (e.g. photos) that don’t also exist on paper on a portable hard drive. Remember to do this for all digital materials that have been saved to your cloud that you might have forgotten about (archived, etc.).<span class="refresh">Refresh when? Do a backup and update every 6 months</span>Note: Since this is time-consuming, put a note in your calendar at the beginning of the year, choosing the time and date when you will do this (as noted in #5 above, you could do this in line with the solstice each year: June 20 and December 20)</li>
    <li>Get a hand cranked radio to ensure you have access to important news and information about what’s happening in your community (locally, as well as nationally/ internationally).<span class="refresh">Refresh when? Make sure the hand cranked radio has fresh batteries (change them every 12 months or so)</span></li>
    <li>Download a copy of your city’s maps (e.g. Wayfind Maps) on your phone for local access, and make sure you have a physical map in case you need to get somewhere new in your city in a rush, and you don’t know how to get there.<span class="refresh">Refresh when: N/A once done</span></li>
  </ol>
</div>

<!-- Cloud storage 3 -->
<header class="header head3" style="top:697px">
  <span class="header-icon"><svg viewBox="0 0 40 40"><path d="M12 14a6 6 0 0 1 11-3 5 5 0 0 1 7 5"/><rect x="6" y="14" width="28" height="20" rx="2"/><path d="M6 19h28"/><circle cx="20" cy="27" r="3"/><path d="M20 22v1.5M20 30.5v1.5M15 27h1.5M23.5 27h1.5"/></svg></span>
  <span class="header-text"><span class="header-title">Information Management</span><span class="header-sub">Cloud storage services have stopped<br>working</span></span>
</header>
<div class="block col3" style="top:768px">
  <p>If you have a smart home device that needs to be connected to the internet to work and that doesn’t have a manual override (e.g. a smart lock for your living space’s main door, or for the garage) ensure you have a backup system in place that would not leave you stranded when the internet goes down.</p>
  <span class="refresh gap-s">Refresh when: N/A once done</span>
</div>

</body>
</html>
```